Electrician Letterhead Design BLR

We need some letterhead for our bills and other papers.
Customer address is on the right side (Swiss format)
A4 format

Design should also be applicable on Cards

Target Market(s)

Private Customers, Small Business

Industry/Entity Type

Electrician

Other font styles liked:
• incised 901

Colors
00AB8E
00BBA5
67D7C9
C6EFE9
E9F9F6

```html
<!DOCTYPE html>
<html lang="de">
<head>
<meta charset="utf-8">
<title>BLR Letterhead</title>
<link href="https://fonts.googleapis.com/css2?family=Arvo&family=Montserrat:wght@600;800&display=swap" rel="stylesheet">
<style>
  :root{
    --backdrop:#dcdcdc;
    --paper:#ffffff;
    --teal:#0aa08f;
    --charcoal:#3d3d3d;
    --ink:#1a1a1a;
    --ghost:#e6e6e6;
    --rule:#9a9a9a;
  }
  html,body{margin:0;padding:0;overflow:hidden}
  body{width:1200px;height:947px;background:var(--backdrop);position:relative}
  .letterhead{position:absolute;left:364px;top:179px;width:472px;height:606px;background:var(--paper);overflow:hidden}
  .brand{position:absolute;left:49px;top:14px}
  .brand-name{font-family:'Montserrat',sans-serif;font-weight:800;font-size:44px;line-height:44px;color:var(--teal);letter-spacing:1px}
  .brand-sub{font-family:'Montserrat',sans-serif;font-weight:600;font-size:7.2px;color:var(--ink);margin-top:2px;letter-spacing:.2px}
  .contact{position:absolute;left:318px;top:23px;padding-left:10px;border-left:1px solid var(--rule);height:31px;display:flex;flex-direction:column;justify-content:space-between}
  .contact-row{display:flex;align-items:center;gap:6px;font-family:'Arvo',serif;font-size:8.6px;line-height:10px;color:var(--ink);margin-top:-1px}
  .contact-row svg{width:8px;height:8px;flex:none}
  .watermark{position:absolute;left:66px;top:220px;font-family:'Montserrat',sans-serif;font-weight:800;font-size:168px;line-height:168px;color:var(--ghost);letter-spacing:4px}
  .footer-waves{position:absolute;left:0;top:0;width:472px;height:606px}
  .address{position:absolute;right:30px;top:578px;font-family:'Arvo',serif;font-size:10.2px;color:#fff}
</style>
</head>
<body>
<div class="letterhead">
  <div class="brand">
    <div class="brand-name">BLR</div>
    <div class="brand-sub">Blitz Leitungen Rhein GmbH</div>
  </div>

  <div class="contact">
    <div class="contact-row">
      <svg viewBox="0 0 10 10"><rect x=".6" y=".6" width="8.8" height="8.8" rx="1.5" fill="none" stroke="var(--teal)" stroke-width="1.1"/><path d="M3.2 2.4c-.6.4-.6 1.4.3 2.6s2 1.8 2.7 1.4l.5-.6-1-.9-.5.4c-.5-.2-1.1-.9-1.2-1.4l.4-.5-.8-1z" fill="var(--teal)"/></svg>
      <span>044-987 654 321</span>
    </div>
    <div class="contact-row">
      <svg viewBox="0 0 10 10"><rect x=".5" y="2" width="9" height="6.5" fill="var(--teal)"/><path d="M.5 2l4.5 3.6L9.5 2M.5 8.5l3.3-3M9.5 8.5l-3.3-3" fill="none" stroke="#fff" stroke-width=".8"/></svg>
      <span>info@blrmail.com</span>
    </div>
    <div class="contact-row">
      <svg viewBox="0 0 10 10" fill="none" stroke="var(--teal)" stroke-width=".8"><circle cx="5" cy="5" r="4.3"/><ellipse cx="5" cy="5" rx="1.9" ry="4.3"/><path d="M.7 5h8.6M1.5 2.8h7M1.5 7.2h7"/></svg>
      <span>www.blr-elektro.com</span>
    </div>
  </div>

  <div class="watermark" aria-hidden="true">BLR</div>

  <svg class="footer-waves" viewBox="0 0 472 606" aria-hidden="true">
    <path d="M0 526C50 556 150 562 283 545C190 560 110 578 0 543Z" fill="var(--charcoal)"/>
    <path d="M0 549C60 570 110 580 180 572C280 562 360 522 472 537L472 606L0 606Z" fill="var(--teal)"/>
  </svg>

  <div class="address">Your Address line here, Country Code 0123456</div>
</div>
</body>
</html>
```